Need a modern, bold, luxurious advertisement flyer for our roofing company. located in buffalo, ny. Big house with a intense roof design asphalt shingles. slogan is "Reliability starts at the top". Colors varies but want it to be modern. we will be handing these out when we are working in the area. phone number is 716-555-0143 for the TRUE PEAK estimate. also our services are roofing, roof repairs, gutters, attic ventilation. we offer a 15 year warranty with our summit shield plan. We are certified by dwellmatch, harlan pike, skarn. Also follow us on facebook, google and yelp. website is tpk-roofing.example, facebook is tpkroofing. pictures are on facebook and our website if need more can be provided. also can include a review we have.

```html
<!DOCTYPE html>
<html lang="en">
<head>
<meta charset="utf-8">
<title>TPK Roofing – Flyer</title>
<link href="https://fonts.googleapis.com/css2?family=Oswald:wght@400;500;600&family=Open+Sans:wght@400;600&display=swap" rel="stylesheet">
<style>
  :root{
    --orange:#f7941d;
    --dark:#1c1c1c;
    --charcoal:#2b2b2b;
    --grey:#5a5d62;
    --text:#4a4a4a;
    --white:#ffffff;
    --star:#f5b400;
  }
  *{margin:0;padding:0;box-sizing:border-box}
  html,body{width:959px;height:1200px;overflow:hidden;background:#e9e9e9}
  .flyer{position:relative;width:959px;height:1200px;background:var(--white);font-family:'Open Sans',sans-serif;color:var(--text);overflow:hidden}
  .abs{position:absolute}

  /* hero */
  .hero{left:0;top:0;width:959px;height:583px;background:radial-gradient(circle at 62% 15%,#4a4a4a 0%,#2a2a2a 35%,#161616 75%)}
  .hero svg{position:absolute;left:0;top:0}
  .brand{left:44px;top:70px;display:flex;align-items:center;gap:14px}
  .brand-mark{width:26px;height:26px;background:var(--orange)}
  .brand-name{font-family:'Oswald',sans-serif;font-weight:500;font-size:40px;letter-spacing:4px;color:var(--orange);line-height:1}
  .social{right:34px;top:22px;display:flex;gap:22px}
  .social span{width:30px;height:30px;border:2px solid #d8d8d8;border-radius:50%}
  .free{right:34px;top:64px;font-family:'Oswald',sans-serif;font-weight:600;font-size:27px;color:var(--orange);letter-spacing:.5px}
  .headline{left:33px;top:248px;font-family:'Oswald',sans-serif;font-weight:500;color:var(--white);font-size:64px;line-height:86px;letter-spacing:.5px;text-shadow:0 2px 6px rgba(0,0,0,.5)}
  .lines{left:36px;top:428px;font-family:'Oswald',sans-serif;font-size:21px;color:var(--orange);letter-spacing:.3px}
  .lines i{font-style:normal;margin:0 9px}
  .seal{left:312px;top:352px;width:110px;height:110px;border-radius:50%;background:radial-gradient(circle,#f4f4f4 0%,#c9c9c9 60%,#9a9a9a 100%);border:4px solid #e6e6e6;box-shadow:0 3px 8px rgba(0,0,0,.5)}

  .choice{left:0;top:540px;width:522px;height:43px;background:var(--orange);border-radius:0 22px 22px 0;font-family:'Oswald',sans-serif;font-size:25px;color:var(--white);line-height:43px;padding-left:36px;letter-spacing:.2px}
  .thumb{width:124px;height:124px;border-radius:50%;border:4px solid var(--white);box-shadow:0 3px 8px rgba(0,0,0,.4);top:476px}

  .intro{left:33px;top:610px;width:896px;font-size:14px;line-height:20px;letter-spacing:-.2px}
  .intro p+p{margin-top:18px}

  /* services */
  .services{left:0;top:756px;width:959px;height:209px;background:linear-gradient(90deg,#3b3633,#2a2725 40%,#1e1e1e 100%);border-top:4px solid var(--orange);border-bottom:4px solid var(--orange)}
  .services-title{left:345px;top:739px;width:270px;height:34px;background:var(--orange);border-radius:17px;font-family:'Oswald',sans-serif;font-weight:500;font-size:26px;color:var(--white);text-align:center;line-height:34px}
  .service-list{left:14px;top:812px;width:930px;display:flex;justify-content:space-between}
  .service{width:112px;text-align:center;font-family:'Oswald',sans-serif;font-size:15px;line-height:21px;color:var(--white)}
  .service svg{display:block;margin:0 auto 10px}

  /* reviews */
  .partners{left:0;top:986px;width:959px;display:flex;justify-content:center;align-items:center;gap:26px}
  .partner{display:flex;align-items:center;gap:6px;font-family:'Open Sans',sans-serif;font-weight:600;font-size:15px;color:var(--charcoal)}
  .partner b{width:12px;height:12px;background:var(--orange)}
  .stars{top:1012px}
  .review{top:1040px;width:436px;font-size:13px;line-height:16px;color:#333}

  .footer{left:0;top:1125px;width:959px;height:75px;background:linear-gradient(90deg,#1a1a1a,#3a3a3a 50%,#1a1a1a)}
  .cta{left:152px;top:1106px;width:652px;height:44px;background:var(--orange);border-radius:12px;font-family:'Oswald',sans-serif;font-size:25px;color:var(--white);display:flex;align-items:center;justify-content:center;gap:10px}
  .web{left:0;top:1162px;width:959px;text-align:center;color:var(--white);font-weight:600;font-size:19px;letter-spacing:1.5px}
</style>
</head>
<body>
<div class="flyer">

  <section class="abs hero">
    <svg width="959" height="583" viewBox="0 0 959 583">
      <defs>
        <linearGradient id="houseTone" x1="0" y1="0" x2="1" y2="0.4">
          <stop offset="0" stop-color="#2a2622"/>
          <stop offset=".45" stop-color="#4b4d52"/>
          <stop offset=".8" stop-color="#6a6c70"/>
          <stop offset="1" stop-color="#8a8b8e"/>
        </linearGradient>
      </defs>
      <polygon role="img" aria-label="Photo of a large house with a dark asphalt shingle roof and dormer window"
               points="0,198 562,198 644,113 959,113 959,583 0,583" fill="url(#houseTone)"/>
      <polyline points="0,200 564,200 646,115 959,115" fill="none" stroke="#ffffff" stroke-width="3"/>
      <polyline points="0,195 560,195 642,110 959,110" fill="none" stroke="#f7941d" stroke-width="2"/>
    </svg>

    <div class="abs brand"><span class="brand-mark"></span><span class="brand-name">TPK ROOFING</span></div>
    <div class="abs social" aria-label="Social links"><span></span><span></span><span></span><span></span></div>
    <div class="abs free">FREE INSPECTIONS</div>

    <h1 class="abs headline">RELIABILITY STARTS<br>AT THE TOP</h1>
    <div class="abs seal" aria-label="15 year summit shield plan warranty seal"></div>
    <div class="abs lines">ROOFING<i>|</i>SIDING<i>|</i>GUTTERS</div>
  </section>

  <div class="abs choice">WE'RE THE RIGHT CHOICE FOR YOUR ROOFING NEEDS</div>
  <div class="abs thumb" style="left:545px;background:linear-gradient(135deg,#8e9296,#5d6166)" role="img" aria-label="Close-up of roof shingles"></div>
  <div class="abs thumb" style="left:686px;background:linear-gradient(135deg,#c9a46a,#b9b3a6 55%,#d8d4cc)" role="img" aria-label="Siding panels being installed"></div>
  <div class="abs thumb" style="left:816px;background:linear-gradient(135deg,#f2f2f2,#cfd3d6)" role="img" aria-label="White gutter and downspout"></div>

  <div class="abs intro">
    <p>By protecting your roof, you're protecting your home and your family, and especially in this area where getting feet upon feet of snow is a common occurrence, you must be able to depend on a roofing contractor to get the job done right.</p>
    <p>Our professionals help keep homes and commercial properties in tip top shape from the outside. If you are looking for a roofer to tackle your upcoming installation or unexpected repair job, choose the one that's earned the title of Harlan Pike Preferred Contractor.</p>
  </div>

  <section class="abs services" role="img" aria-label="Background photo of a roofer's gloved hands laying shingles"></section>
  <div class="abs services-title">OUR SERVICES</div>

  <div class="abs service-list">
    <div class="service"><svg width="64" height="64" viewBox="0 0 64 64"><circle cx="32" cy="32" r="30" fill="#f7941d" stroke="#fff" stroke-width="3"/><path d="M16 42 L32 24 L48 42 Z" fill="#1c1c1c"/></svg>ROOF<br>INSTALLATION<br>AND REPAIR</div>
    <div class="service"><svg width="64" height="64" viewBox="0 0 64 64"><circle cx="32" cy="32" r="30" fill="#f7941d" stroke="#fff" stroke-width="3"/><path d="M16 30 L32 20 L48 30 L32 40 Z M16 36 L32 46 L48 36" fill="none" stroke="#fff" stroke-width="3"/></svg>ATTIC<br>VENTILATION</div>
    <div class="service"><svg width="64" height="64" viewBox="0 0 64 64"><circle cx="32" cy="32" r="30" fill="#f7941d" stroke="#fff" stroke-width="3"/><path d="M12 40 L28 22 L36 30 L40 26 L52 40 Z" fill="#fff"/></svg>RE-ROOF</div>
    <div class="service"><svg width="64" height="64" viewBox="0 0 64 64"><circle cx="32" cy="32" r="30" fill="#f7941d" stroke="#fff" stroke-width="3"/><rect x="18" y="28" width="12" height="18" fill="#1c1c1c"/><rect x="32" y="18" width="14" height="28" fill="#1c1c1c"/></svg>COMMERCIAL<br>ROOFING</div>
    <div class="service"><svg width="64" height="64" viewBox="0 0 64 64"><circle cx="32" cy="32" r="30" fill="#f7941d" stroke="#fff" stroke-width="3"/><rect x="20" y="20" width="18" height="24" fill="#fff"/><path d="M24 28 h10 M24 33 h10 M24 38 h6" stroke="#1c1c1c" stroke-width="2"/><path d="M38 44 l6-12 4 2 -6 12 z" fill="#1c1c1c"/></svg>ROOF<br>INSPECTION</div>
    <div class="service"><svg width="64" height="64" viewBox="0 0 64 64"><circle cx="32" cy="32" r="30" fill="#f7941d" stroke="#fff" stroke-width="3"/><path d="M18 22 h28 M18 30 h28 M18 38 h28 M18 46 h28" stroke="#fff" stroke-width="5"/></svg>SIDING<br>REPAIR</div>
    <div class="service"><svg width="64" height="64" viewBox="0 0 64 64"><circle cx="32" cy="32" r="30" fill="#f7941d" stroke="#fff" stroke-width="3"/><path d="M14 32 L32 16 L50 32 L46 32 L46 48 L18 48 L18 32 Z" fill="#fff"/><path d="M26 42 L38 30 M26 30 L38 42" stroke="#1c1c1c" stroke-width="3"/></svg>NEW SIDING<br>INSTALLATION</div>
    <div class="service"><svg width="64" height="64" viewBox="0 0 64 64"><circle cx="32" cy="32" r="30" fill="#f7941d" stroke="#fff" stroke-width="3"/><path d="M16 22 h32 v8 h-14 v16 h-8 v-16 h-10 z" fill="#fff"/></svg>GUTTERS</div>
  </div>

  <div class="abs partners">
    <span class="partner"><b></b>dwellmatch</span>
    <span class="partner">SKARN</span>
    <span class="partner">harlan pike</span>
  </div>

  <svg class="abs stars" style="left:30px" width="124" height="22" viewBox="0 0 124 22" aria-label="Five stars"><g fill="#f5b400">
    <polygon id="st" points="11,1 14,8 21,8 15.5,12.5 17.5,20 11,15.5 4.5,20 6.5,12.5 1,8 8,8"/>
    <use href="#st" x="25"/><use href="#st" x="50"/><use href="#st" x="75"/><use href="#st" x="100"/></g></svg>
  <svg class="abs stars" style="left:805px" width="124" height="22" viewBox="0 0 124 22" aria-label="Five stars"><g fill="#f5b400">
    <use href="#st"/><use href="#st" x="25"/><use href="#st" x="50"/><use href="#st" x="75"/><use href="#st" x="100"/></g></svg>

  <p class="abs review" style="left:33px">TPK is an awesome company to work with, and we highly, highly recommend them!! We hired them to do a full tear off of our roof, and we are so very glad we did!!</p>
  <p class="abs review" style="left:494px">During this last wind storm, the roofing companies we called were completely booked for weeks. I saw the TPK truck in my neighbor-hood and ran right over.</p>

  <footer class="abs footer"></footer>
  <div class="abs cta">CALL TPK ROOFING
    <svg width="20" height="20" viewBox="0 0 20 20" aria-hidden="true"><circle cx="10" cy="10" r="8.5" fill="none" stroke="#fff" stroke-width="1.6"/><path d="M7 5.5 l2 2 -1 1.5 c.8 1.5 1.6 2.3 3 3 l1.5-1 2 2 -1.2 1.5 c-3.5-.5-7-4-7.5-7.5 z" fill="#fff"/></svg>
    716-555-0143 FOR YOUR FREE ESTIMATE</div>
  <div class="abs web">www.tpk-roofing.example</div>

</div>
</body>
</html>
```